Need business card designed for a Mobile RV Repair business

I need a business card designed

Welding sparks

Industry/Entity Type

Rv Repair , Mobile Welding & Fabrication

Contact Information for Business Card

****

Colors
0054AA
0677BA
7BADD7
CADEEF
E8F1F8

Requirements
Nice to have
• welding sparks, list of services, welding vector

```html
<!DOCTYPE html>
<html lang="en">
<head>
<meta charset="utf-8">
<title>K&amp;M Mobile RV &amp; Motorhome Repair – Business Card</title>
<link rel="stylesheet" href="https://fonts.googleapis.com/css2?family=Poppins:wght@400;500;700&display=swap">
<style>
  :root {
    --brand-blue: #0054aa;
    --brand-mid: #0677ba;
    --brand-soft: #7badd7;
    --brand-pale: #cadeef;
    --brand-mist: #e8f1f8;
    --ink: #0b2340;
    --paper: #ffffff;
    --stage: #2a2a2a;
  }
  * { box-sizing: border-box; margin: 0; padding: 0; }
  html, body { width: 1200px; height: 1015px; overflow: hidden; }
  body {
    background: var(--stage);
    font-family: "Poppins", sans-serif;
    position: relative;
  }
  .card {
    position: absolute;
    left: 250px;
    width: 700px;
    height: 400px;
    overflow: hidden;
    box-shadow: 0 10px 30px rgba(0,0,0,.5);
  }

  /* Front side */
  .card--front { top: 60px; background: var(--brand-blue); color: var(--paper); }
  .card--front .brand-name {
    position: absolute; top: 40px; left: 0; right: 0;
    text-align: center; font-weight: 500; font-size: 32px; line-height: 1.15;
    color: var(--paper);
  }
  .photo-strip {
    position: absolute; top: 150px; left: 0; right: 0; height: 120px;
    display: flex; gap: 3px; background: var(--brand-mist); padding: 3px 0;
  }
  .photo-strip .photo {
    flex: 1;
    background: linear-gradient(160deg, var(--brand-pale), var(--brand-mid));
  }
  .services {
    position: absolute; top: 288px; left: 0; right: 0;
    text-align: center; font-size: 17px; line-height: 1.45; font-weight: 400;
  }
  .services span { margin: 0 10px; }

  /* Back side */
  .card--back { top: 555px; background: var(--paper); }
  .card--back .brand-name {
    position: absolute; top: 66px; left: 0; right: 0;
    text-align: center; font-weight: 500; font-size: 36px; line-height: 1.15;
    color: var(--ink);
  }
  .contact-band {
    position: absolute; top: 205px; left: 0; right: 0; height: 150px;
    background: var(--brand-mid); color: var(--paper);
    text-align: center; padding-top: 16px;
  }
  .contact-band .person { font-weight: 700; font-size: 26px; line-height: 1.1; }
  .contact-band .role { font-size: 15px; }
  .contact-band .rule {
    width: 130px; height: 1px; background: var(--brand-pale);
    margin: 6px auto 6px;
  }
  .contact-band .detail { font-size: 16px; line-height: 1.45; }
</style>
</head>
<body>
  <section class="card card--front" aria-label="Card front">
    <h1 class="brand-name">K&amp;M Mobile RV &amp;<br>Motorhome Repair</h1>
    <div class="photo-strip">
      <div class="photo" role="img" aria-label="Photo of a finished trailer interior"></div>
      <div class="photo" role="img" aria-label="Photo of a steel frame under fabrication"></div>
      <div class="photo" role="img" aria-label="Photo of a custom aluminium trailer ramp"></div>
      <div class="photo" role="img" aria-label="Photo of a white RV trailer parked outside"></div>
    </div>
    <p class="services">
      <span>RV Repair</span><span>Welding</span><span>Metal fabrication</span><span>Mobile RV and</span><br>
      <span>Motorhome Repairs</span><span>Mobile welding</span><span>Building custom trailers</span><br>
      <span>Fabricating new products and equipment</span><span>Gates/fences</span>
    </p>
  </section>

  <section class="card card--back" aria-label="Card back">
    <h2 class="brand-name">K&amp;M Mobile RV &amp;<br>Motorhome Repair</h2>
    <div class="contact-band">
      <p class="person">Dale Brennan</p>
      <p class="role">Owner</p>
      <div class="rule"></div>
      <p class="detail">555.210.4478</p>
      <p class="detail">kmmobilerv@example.com</p>
    </div>
  </section>
</body>
</html>
```